IT Services Business Card Design

We require a business card design for an IT services company called RT Program Freightworks.

We specialize in taking an organisations software and readying it for deployment to new environments (e.g. Zen qa to Zen 4). This process is termed application packaging. This is not the same as putting things in boxes but I am happy to use boxes as a pun icon ;-) This is our second step in branding, we currently have a new logo and our poor excuse of a website is next to be updated but it contains information on who we are and what we cover at rtprogramfreightworks.example

We are looking for a fun, modern but stylish and professional looking design.

I have attached the logo in multiple formats including vector formats (and the fonts that created the logo if required)
Updates

Thanks to all the designers so far, some great designs in there.  I will be selecting a card design on the deadline date. 

However, there is still time to submit some more designs.  The majority of the ones I have so far are typical simplistic designs that we have all seen before and I have enough of those to choose from now.  If you wish to submit any more designs, please submit somthing unusual to grab our attention.

Target Market(s)

Project executives of large organisations looking for Panecraft migrations

Industry/Entity Type

Software

Requirements
Must have
• Want to show company name, contact name, title, main number, contact number, fax number, email address and website address. I do not want to show the address.
Must use the attached logo, retaining the colours in them.

This has to be a double-sided design. I will be using lark.example and will be selecting their rounded corner business card design.

Their templates and design requirements (sizing etc.) can be found here: http://uk.lark.example/help/faq/templates-and-guidelines.html

Happy for company name or website to be on either side of the card.

This design has to be original and not used before for another company

Would like to style it around the business colours in the logo
Nice to have
• Lark.example has an option for multiple card designs to appear on the back. If this is possible in the budget and time you have and you have a design(s) that work with that but carry the same style and theme, that would be nice to see but not necessary.
Should not have
• We do not want to put a postal address on the cards

```html
<!DOCTYPE html>
<html lang="en">
<head>
<meta charset="utf-8">
<title>RT Program Freightworks – Business Card</title>
<link href="https://fonts.googleapis.com/css2?family=Open+Sans:wght@300;400;700&display=swap" rel="stylesheet">
<style>
  :root {
    --stage: #161616;
    --card-white: #ffffff;
    --card-dark: #262c2b;
    --band-grey: #f1f1f3;
    --brand-blue: #4a6fba;
    --ink-warm: #5b5650;
    --ink-grey: #6f6f6f;
    --ink-light: #d9dbdb;
  }
  * { margin: 0; padding: 0; box-sizing: border-box; }
  html, body { width: 1200px; height: 1000px; overflow: hidden; }
  body {
    background: var(--stage);
    font-family: "Open Sans", Arial, sans-serif;
    position: relative;
  }
  .card {
    position: absolute;
    left: 360px;
    width: 480px;
    height: 314px;
    overflow: hidden;
  }
  .card--front { top: 146px; background: var(--card-white); }
  .card--back  { top: 540px; background: var(--card-dark); }

  .card__band { position: absolute; inset: 0; }

  .wordmark {
    position: absolute;
    display: flex;
    align-items: center;
    gap: 10px;
    font-weight: 300;
    white-space: nowrap;
  }
  .wordmark__dot {
    width: 34px; height: 34px;
    border-radius: 50%;
    background: var(--brand-blue);
    flex: none;
  }
  .card--front .wordmark {
    left: 28px; top: 50px;
    font-size: 22px;
    color: var(--ink-warm);
  }
  .card--back .wordmark {
    left: 0; right: 0; top: 136px;
    justify-content: center;
    font-size: 26px;
    color: var(--ink-light);
  }

  .contact {
    position: absolute;
    left: 92px;
    top: 158px;
    color: var(--ink-grey);
  }
  .contact__name {
    font-size: 17px;
    font-weight: 700;
    color: var(--brand-blue);
    letter-spacing: 0.2px;
  }
  .contact__title { font-size: 12.5px; margin-top: 1px; }
  .contact__list { list-style: none; margin-top: 14px; font-size: 12.5px; line-height: 18.5px; }
  .contact__label {
    display: inline-block;
    width: 17px;
    font-weight: 700;
    color: var(--brand-blue);
  }
  .contact__web { font-size: 12.5px; margin-top: 10px; }

  .card__web {
    position: absolute;
    left: 0; right: 0; top: 228px;
    text-align: center;
    font-size: 12.5px;
    letter-spacing: 1px;
    color: var(--ink-light);
  }
</style>
</head>
<body>

<section class="card card--front" aria-label="Card front">
  <svg class="card__band" width="480" height="314" viewBox="0 0 480 314" aria-hidden="true">
    <path d="M0 262 C120 200 300 170 480 172 L480 314 L0 314 Z" fill="var(--band-grey)"/>
  </svg>

  <div class="wordmark">
    <span>RT Program Freightworks</span>
    <span class="wordmark__dot"></span>
  </div>

  <div class="contact">
    <p class="contact__name">YOUR NAME HERE</p>
    <p class="contact__title">Title Goes Here</p>
    <ul class="contact__list">
      <li><span class="contact__label">T</span>+62 800 555 0142</li>
      <li><span class="contact__label">F</span>+62 800 555 0187</li>
      <li><span class="contact__label">E</span>enquiries@rtprogramfreightworks.example</li>
    </ul>
    <p class="contact__web">www.rtprogramfreightworks.example</p>
  </div>
</section>

<section class="card card--back" aria-label="Card back">
  <div class="wordmark">
    <span>RT Program Freightworks</span>
    <span class="wordmark__dot"></span>
  </div>
  <p class="card__web">www.rtprogramfreightworks.example</p>
</section>

</body>
</html>
```